Business Card Design

we need a business card as well as a logo that can be used for signs etc.
this is a very formal, classy , elegant function centre, as well as café. I am after a design that stands out and grabs people attentions. my colours theme is really warm ,colours like chocolate browns, and latte type colours with really deep red tones
not bright red, just warm tones. this is a place that very wealthy and maybe even celebs will come so I need it to be appealing.
Industry/Entity Type
Business
Contact Information for Business Card
Grey Finch
café and function centre @ haldons estate.
wedding and function specialists,
Corbett highway, lucknow,ph 0427385190

```html
<!DOCTYPE html>
<html lang="en">
<head>
<meta charset="utf-8">
<title>Grey Finch – Business Card</title>
<link rel="stylesheet" href="https://fonts.googleapis.com/css2?family=Roboto+Slab:wght@500;600&display=swap">
<style>
  :root {
    --page-bg: #efefef;
    --latte: #c9a06a;
    --chocolate: #4a3223;
    --ink: #4b3122;
  }
  * { margin: 0; padding: 0; box-sizing: border-box; }
  html, body {
    width: 1200px;
    height: 1200px;
    overflow: hidden;
    background: var(--page-bg);
  }
  .canvas {
    position: relative;
    width: 1200px;
    height: 1200px;
  }
  .business-card {
    position: absolute;
    left: 253px;
    top: 385px;
    width: 694px;
    height: 431px;
    background: var(--latte);
    overflow: hidden;
    font-family: "Roboto Slab", Georgia, serif;
    color: var(--ink);
  }
  .card-band {
    position: absolute;
    inset: 0;
    width: 694px;
    height: 431px;
  }
  .card-band path { fill: var(--chocolate); }
  .brand-mark {
    position: absolute;
    left: 24px;
    top: 142px;
    width: 250px;
    height: 60px;
    display: flex;
    align-items: center;
    justify-content: center;
    gap: 14px;
  }
  .brand-mark .brand-dot {
    width: 34px;
    height: 34px;
    border-radius: 50%;
    background: var(--ink);
    flex: none;
  }
  .brand-mark .brand-name {
    font-size: 34px;
    font-weight: 600;
    color: var(--ink);
    white-space: nowrap;
  }
  .venue-details {
    position: absolute;
    left: 300px;
    width: 400px;
    top: 50px;
    text-align: center;
  }
  .venue-name {
    font-size: 32px;
    font-weight: 600;
    line-height: 1.1;
  }
  .venue-tagline {
    margin-top: 12px;
    font-size: 19px;
    font-weight: 500;
  }
  .venue-address {
    margin-top: 58px;
    font-size: 29px;
    font-weight: 600;
    line-height: 1.7;
  }
  .venue-phone {
    position: absolute;
    left: 300px;
    width: 400px;
    top: 352px;
    text-align: center;
    font-size: 35px;
    font-weight: 600;
    color: var(--latte);
    white-space: nowrap;
  }
</style>
</head>
<body>
<main class="canvas">
  <article class="business-card">
    <svg class="card-band" viewBox="0 0 694 431" aria-hidden="true">
      <path d="M0 378 C 180 338, 380 300, 694 312 L694 431 L0 431 Z"/>
    </svg>

    <div class="brand-mark">
      <span class="brand-dot"></span>
      <span class="brand-name">Grey Finch</span>
    </div>

    <div class="venue-details">
      <h1 class="venue-name">Haldons Estate</h1>
      <p class="venue-tagline">wedding and function specialists</p>
      <p class="venue-address">Corbett highway<br>Ashbury</p>
    </div>

    <p class="venue-phone">Phone: 0427385190</p>
  </article>
</main>
</body>
</html>
```